Flyer-Design für Geburtstagsglückwunsch-Postkarte
Zielgruppe
Unter www.kelvarisen.de bieten wir im Großraum Stuttgart Städtereisen in europäische Metropolen an (hauptsächlich mit dem Bus), außerdem Eventreisen, Erlebnisreisen, Strandreisen und im Winter Skiausfahrten und Silvesterreisen sowie ganzjährig Gruppenreisen für Vereine und Betriebe an. Zielgruppe recht gemischt vorwiegend jung (18-40 Jahre), Ansprache auf Website und im Schriftverkehr mit 'Sie'. Anbei unser Logo.
Aufgabenstellung
Wir möchten unseren Kunden zum Geburtstag eine Postkarte (Klassisches Format DIn6 148 x 105) senden. Voderseite bunt (schönes Bild + Happy Birthday + kelvarisen wünscht Ihnen alles Gute zum Geburtstag, unser Logo, evtl. www.kelvarisen.de > klein) und Rückseite mit Glückwünschen in s/w (rechts platz für Postkarte oben und anschrift des Kunden > wird von uns handschriftlich hinzugefügt // links dann nette Geburtstagsglückwünsche bereits gedruckt und klein unsere Anschrift kelvarisen GmbH, www.kelvarisen.de). Für Ihre Ideen für eine schöne innovative Geburtstags-Postkarte sind wir offen.

```html
<!DOCTYPE html>
<html lang="de">
<head>
<meta charset="utf-8">
<title>kelvarisen – Geburtstagskarten</title>
<link rel="stylesheet" href="https://fonts.googleapis.com/css2?family=Gochi+Hand&family=Courier+Prime:wght@400;700&display=swap">
<style>
  :root {
    --page: #ffffff;
    --brand-blue: #3a6aa6;
    --brand-navy: #2f5f9e;
    --headline-yellow: #f5e21e;
    --headline-purple: #5a3d98;
    --headline-red: #d8262b;
    --text-ink: #3e5d86;
    --text-dark: #2d3a4a;
    --panel-cream: #fbf8ee;
    --card-shadow: rgba(0,0,0,.35);
  }
  * { margin: 0; padding: 0; box-sizing: border-box; }
  html, body { width: 1200px; height: 5106px; overflow: hidden; background: var(--page); }
  body { position: relative; font-family: "Courier Prime", "Courier New", monospace; }

  .card {
    position: absolute; left: 40px; width: 1130px; height: 796px;
    overflow: hidden; box-shadow: 0 3px 8px var(--card-shadow);
  }
  .card--sky { top: 32px; }
  .card--comic { top: 886px; }
  .card--cupcake { top: 1740px; }
  .card--puppy { top: 2594px; }
  .card--party { top: 3448px; }
  .card--clover { top: 4302px; }

  .artwork { position: absolute; inset: 0; }
  .artwork--sky { background: linear-gradient(180deg, #2f73c9 0%, #6aa3dc 38%, #d9e6f1 70%, #eef1f4 100%); }
  .artwork--balloons { inset: auto; left: 60px; top: 14px; width: 300px; height: 760px;
    background: radial-gradient(ellipse 45% 22% at 50% 20%, #f07fb0, #6fc9d6 55%, transparent 70%); }
  .artwork--comic { background: linear-gradient(135deg, #ff4fa3 0%, #ffd21f 30%, #2bb5e8 55%, #ff7a1a 78%, #8c3fc4 100%); }
  .artwork--teal { background: linear-gradient(180deg, #4e8e99 0%, #6ea8b1 60%, #dfe4e4 78%, #eef0ef 100%); }
  .artwork--cupcake { inset: auto; left: 190px; top: 300px; width: 360px; height: 460px;
    background: radial-gradient(ellipse 50% 40% at 50% 40%, #f38cb0, #e35b8e 60%, transparent 75%); }
  .artwork--white { background: #ffffff; }
  .artwork--puppy { inset: auto; left: 0; top: 30px; width: 700px; height: 766px;
    background: radial-gradient(ellipse 55% 45% at 40% 60%, #b06a3a, #c9874f 55%, transparent 75%); }
  .artwork--party { background: radial-gradient(ellipse at 50% 55%, #f7c76a 0%, #d9603f 35%, #8a2a46 65%, #3c1a3a 100%); }
  .artwork--wood { background: linear-gradient(180deg, #f1f2f3 0%, #dde0e2 55%, #cfd3d6 100%); }
  .artwork--clover { inset: auto; left: 70px; top: 400px; width: 460px; height: 380px;
    background: radial-gradient(circle at 50% 50%, #2c1a12 0%, #3d8a22 30%, #5fae2e 55%, transparent 72%); }

  .headline {
    position: absolute; font-family: "Gochi Hand", cursive;
    font-weight: 400; line-height: .98; letter-spacing: 2px;
  }
  .headline--stacked { right: 50px; top: 30px; font-size: 142px; text-align: right; }
  .headline--line { left: 76px; top: 46px; font-size: 112px; white-space: nowrap; }
  .headline--yellow { color: var(--headline-yellow); }
  .headline--blue { color: var(--brand-blue); }

  .wish {
    position: absolute; color: var(--text-ink); font-size: 29px; line-height: 50px;
    letter-spacing: 1px; text-align: right; white-space: pre;
  }
  .wish--right { right: 54px; top: 318px; }
  .wish--stagger { left: 760px; top: 186px; text-align: left; line-height: 42px; }
  .wish--light { color: #f2f5f7; }

  .brand-box {
    position: absolute; right: 0; top: 584px; width: 420px; height: 180px;
  }
  .brand-box__plate {
    position: absolute; left: 0; top: 0; width: 420px; height: 132px;
    background: #fff; border-radius: 28px 0 0 28px;
  }
  .brand-box--outlined .brand-box__plate { border: 3px solid var(--brand-navy); border-right: 0; }
  .brand-box__url {
    position: absolute; left: 60px; top: 132px; width: 360px; height: 46px;
    background: var(--brand-navy); border-radius: 0 0 0 22px;
    color: #fff; font-weight: 700; font-size: 25px; line-height: 46px;
    text-align: center; letter-spacing: 1px;
  }
  .brand {
    position: absolute; display: flex; align-items: center; gap: 18px;
  }
  .brand-box .brand { left: 44px; top: 0; height: 132px; }
  .brand__square {
    width: 26px; height: 26px; background: var(--brand-blue); flex: none;
  }
  .brand__name {
    color: var(--brand-blue); font-weight: 700;
    font-size: 42px; line-height: 44px;
  }

  .comic-panel {
    position: absolute; left: 150px; top: 50px; width: 820px; height: 660px;
    background: var(--panel-cream); box-shadow: 0 0 0 4px #222;
  }
  .comic-panel .headline { left: 0; right: 0; top: 56px; text-align: center; font-size: 136px; color: var(--headline-purple); }
  .comic-panel .wish { left: 0; right: 0; top: 388px; text-align: center; color: var(--text-dark); font-size: 31px; line-height: 42px; }
  .comic-panel .brand { left: 0; right: 0; top: 520px; justify-content: center; }

  .party-banner {
    position: absolute; left: 370px; top: 0; width: 760px; height: 136px;
    background: var(--headline-yellow);
  }
  .party-banner .headline { left: 30px; top: 12px; font-size: 72px; color: var(--headline-red); }
  .party-banner__wish {
    position: absolute; left: 20px; top: 94px; font-size: 20px;
    color: var(--text-dark); white-space: nowrap;
  }
</style>
</head>
<body>

<section class="card card--sky">
  <div class="artwork artwork--sky" role="img" aria-label="Himmel mit Wolken"></div>
  <div class="artwork artwork--balloons" role="img" aria-label="Frau mit Koffer schwebt an einem bunten Luftballonbündel"></div>
  <h2 class="headline headline--stacked headline--yellow">HAPPY<br>BIRTHDAY!</h2>
  <p class="wish wish--right">kelvarisen wünscht
Ihnen alles Gute
zum Geburtstag</p>
  <div class="brand-box">
    <div class="brand-box__plate"></div>
    <div class="brand"><span class="brand__square"></span><span class="brand__name">kelvarisen</span></div>
    <div class="brand-box__url">www.kelvarisen.de</div>
  </div>
</section>

<section class="card card--comic">
  <div class="artwork artwork--comic" role="img" aria-label="Bunter Pop-Art-Comic-Hintergrund mit Sprechblasen und Sternen"></div>
  <div class="comic-panel">
    <h2 class="headline">HAPPY<br>BIRTHDAY!</h2>
    <p class="wish">kelvarisen wünscht Ihnen
alles Gute zum Geburtstag</p>
    <div class="brand"><span class="brand__square"></span><span class="brand__name">kelvarisen</span></div>
  </div>
</section>

<section class="card card--cupcake">
  <div class="artwork artwork--teal" role="img" aria-label="Petrolfarbener Hintergrund auf weißem Tisch"></div>
  <div class="artwork artwork--cupcake" role="img" aria-label="Rosa Cupcake mit Kirsche und türkiser Schleife"></div>
  <h2 class="headline headline--line headline--yellow">HAPPY BIRTHDAY!</h2>
  <p class="wish wish--stagger wish--light">kelvarisen
   wünscht Ihnen
 alles Gute
  zum Geburtstag</p>
  <div class="brand-box">
    <div class="brand-box__plate"></div>
    <div class="brand"><span class="brand__square"></span><span class="brand__name">kelvarisen</span></div>
    <div class="brand-box__url">www.kelvarisen.de</div>
  </div>
</section>

<section class="card card--puppy">
  <div class="artwork artwork--white"></div>
  <div class="artwork artwork--puppy" role="img" aria-label="Welpe mit Partyhut neben einem Cupcake mit Kerze"></div>
  <h2 class="headline headline--stacked headline--blue">HAPPY<br>BIRTHDAY!</h2>
  <p class="wish wish--right">kelvarisen wünscht
Ihnen alles Gute
zum Geburtstag</p>
  <div class="brand-box brand-box--outlined">
    <div class="brand-box__plate"></div>
    <div class="brand"><span class="brand__square"></span><span class="brand__name">kelvarisen</span></div>
    <div class="brand-box__url">www.kelvarisen.de</div>
  </div>
</section>

<section class="card card--party">
  <div class="artwork artwork--party" role="img" aria-label="Feiernde Freunde stoßen mit Sektgläsern an, bunte Lichter"></div>
  <div class="party-banner">
    <h2 class="headline">HAPPY BIRTHDAY!</h2>
    <p class="party-banner__wish">kelvarisen wünscht Ihnen alles Gute zum Geburtstag</p>
  </div>
  <div class="brand-box">
    <div class="brand-box__plate"></div>
    <div class="brand"><span class="brand__square"></span><span class="brand__name">kelvarisen</span></div>
    <div class="brand-box__url">www.kelvarisen.de</div>
  </div>
</section>

<section class="card card--clover">
  <div class="artwork artwork--wood" role="img" aria-label="Hellgraue Holzoberfläche"></div>
  <div class="artwork artwork--clover" role="img" aria-label="Vierblättriges Kleeblatt"></div>
  <h2 class="headline headline--line headline--blue">HAPPY BIRTHDAY!</h2>
  <p class="wish wish--stagger">kelvarisen
   wünscht Ihnen
 alles Gute
  zum Geburtstag</p>
  <div class="brand-box">
    <div class="brand-box__plate"></div>
    <div class="brand"><span class="brand__square"></span><span class="brand__name">kelvarisen</span></div>
    <div class="brand-box__url">www.kelvarisen.de</div>
  </div>
</section>

</body>
</html>
```